Business Card Design

We need two business cards - same design but with two different people's details.

We are a new start-up online cleaning business that allows people to book and pay for a quality home cleaner online.

We would like a professional yet overly formal style of business card.

Target Market(s)

18 - 65+ professionals

Industry/Entity Type

Business

Contact Information for Business Card

We would like two business cards but with the same design, the details are below:

Mark Pelletta
Director and Co-Founder
ph: 0491 352 807
Suite 4C, Level 3
517 Larkfield Road
Brindale NSW 2093
mark@tidvane.com.au

_______________________________________________________

Evadne Pelletta
Director and Co-Founder
ph: 0427 915364
Suite 4C, Level 3
517 Larkfield Road
Brindale NSW 2093
evadne@tidvane.com.au

Requirements
Must have
• although our style guide refers to orange and red, please stick to the blue/black/grey that is in the style guide.

also on the back of the card we would like the logo with our tag line which is on page 12 of the style guide.
Should not have
• no pictures of mops, cleaners etc

```html
<!DOCTYPE html>
<html lang="en">
<head>
<meta charset="utf-8">
<title>Tidvane Business Cards</title>
<link rel="stylesheet" href="https://fonts.googleapis.com/css2?family=Josefin+Sans:wght@300;400;600&family=Indie+Flower&display=swap">
<style>
  :root {
    --stage: #e9e8e6;
    --card: #f7f6f3;
    --card-back: #ffffff;
    --band: #c9c9c9;
    --rule: #d3d2cf;
    --ink-soft: #8d8c89;
    --ink: #5a5a5a;
    --ink-dark: #3e4348;
    --shadow: rgba(0,0,0,0.18);
  }
  * { box-sizing: border-box; margin: 0; padding: 0; }
  html, body {
    width: 1200px; height: 900px; overflow: hidden;
    background: var(--stage);
    font-family: "Josefin Sans", "Helvetica Neue", Arial, sans-serif;
  }
  .stage { position: relative; width: 1200px; height: 900px; }

  .card {
    position: absolute;
    width: 540px; height: 309px;
    background: var(--card);
    box-shadow: 0 10px 24px var(--shadow);
    overflow: hidden;
  }
  .card--mark   { left: 45px;  top: 70px; }
  .card--evadne { left: 615px; top: 70px; }
  .card--back   { left: 330px; top: 510px; background: var(--card-back); }

  .rule { position: absolute; background: var(--rule); }
  .rule--top    { left: 30px; right: 30px; top: 105px; height: 1px; }
  .rule--bottom { left: 30px; right: 30px; top: 192px; height: 1px; }
  .rule--divide { left: 300px; top: 105px; width: 1px; height: 87px; }

  .person { position: absolute; left: 40px; top: 124px; width: 255px; }
  .person__name {
    font-weight: 300; font-size: 25px; letter-spacing: 0.5px;
    text-transform: uppercase; color: var(--ink-soft); white-space: nowrap;
  }
  .person__title {
    margin-top: 8px; font-weight: 400; font-size: 15px;
    text-transform: uppercase; color: var(--ink-dark); letter-spacing: 0.3px;
  }

  .contact { position: absolute; left: 320px; top: 122px; }
  .contact__phone {
    font-weight: 400; font-size: 19px; letter-spacing: 2px; color: var(--ink);
  }
  .contact__email {
    margin-top: 12px; font-size: 11px; letter-spacing: 0.5px;
    text-transform: uppercase; color: var(--ink);
  }

  .address {
    position: absolute; left: 0; right: 0; top: 214px; text-align: center;
    font-size: 13px; letter-spacing: 0.5px; text-transform: uppercase; color: var(--ink);
  }

  .back__band { position: absolute; inset: 0; }
  .back__tagline {
    position: absolute; left: 0; right: 0; top: 130px; text-align: center;
    font-family: "Indie Flower", cursive; font-size: 20px; color: var(--ink);
  }
  .back__brand {
    position: absolute; right: 40px; bottom: 28px;
    font-weight: 600; font-size: 20px; color: var(--ink-dark);
  }
</style>
</head>
<body>
<main class="stage">

  <section class="card card--mark" aria-label="Business card front, Mark Pelletta">
    <div class="rule rule--top"></div>
    <div class="rule rule--divide"></div>
    <div class="rule rule--bottom"></div>
    <div class="person">
      <p class="person__name">Mark Pelletta</p>
      <p class="person__title">Director and Co-Founder</p>
    </div>
    <div class="contact">
      <p class="contact__phone">0491 352 807</p>
      <p class="contact__email">mark@tidvane.com.au</p>
    </div>
    <p class="address">Suite 4C, Level 3 517 Larkfield Road Brindale NSW 2093</p>
  </section>

  <section class="card card--evadne" aria-label="Business card front, Evadne Pelletta">
    <div class="rule rule--top"></div>
    <div class="rule rule--divide"></div>
    <div class="rule rule--bottom"></div>
    <div class="person">
      <p class="person__name">Evadne Pelletta</p>
      <p class="person__title">Director and Co-Founder</p>
    </div>
    <div class="contact">
      <p class="contact__phone">0427 915364</p>
      <p class="contact__email">evadne@tidvane.com.au</p>
    </div>
    <p class="address">Suite 4C, Level 3 517 Larkfield Road Brindale NSW 2093</p>
  </section>

  <section class="card card--back" aria-label="Business card back">
    <svg class="back__band" width="540" height="309" viewBox="0 0 540 309" aria-hidden="true">
      <polygon points="0,0 540,0 540,40 0,270" fill="var(--band)"/>
    </svg>
    <p class="back__tagline">Save time. Book a quality cleaner online.</p>
    <p class="back__brand">Tidvane.com.au</p>
  </section>

</main>
</body>
</html>
```